Round box die line design of photo-realistic prescription medicine bottle

We sell unique products for drinking enthusiasts and we’re in search of a designer to collaborate with us on gag designs for our round gift boxes for wine and booze bottles.

Our initial product will be designed to look like a pharmacy pill bottle with a prescription sticker. I’ve included examples of the pill bottles as well as the “prescription.”

I’ve also attached a picture of an existing paper tube for wine as it’s probably easier to see an actual image than trying to picture it from my terrible description.

This design needs to cover the entire paper tube approximately 13.5 inches by 7.5 inches

Thank you in advance for taking the time to look at my project request. Please feel free to reach out with any questions.

Target Market(s)

The life of the party

Industry/Entity Type

ecommerce

Colors
EE7325
F08F49
F5BC92
FAE3D3
FDF4ED

Requirements
Must have
• Look at realistic as possible
Should not have
• a label design just uploaded to an existing 3d template

```html
<!DOCTYPE html>
<html lang="en">
<head>
<meta charset="utf-8">
<title>Prescription Strength Vino – Tube Wrap</title>
<link href="https://fonts.googleapis.com/css2?family=Oswald:wght@700&family=Roboto+Mono:wght@400;500;700&display=swap" rel="stylesheet">
<style>
  :root {
    --page: #ffffff;
    --orange: #e2621f;
    --orange-deep: #c34a1a;
    --orange-light: #ee7325;
    --highlight: #f5bc92;
    --cap-white: #f4f6f7;
    --cap-ridge: #d6dadd;
    --label: #ffffff;
    --ink: #151515;
    --yellow: #f7e600;
    --box-line: #ee7325;
    --stamp: #a3262a;
  }
  * { margin: 0; padding: 0; box-sizing: border-box; }
  html, body { width: 1200px; height: 604px; overflow: hidden; background: var(--page); }
  .wrap-artwork {
    position: absolute; left: 80px; top: 13px; width: 1040px; height: 578px; overflow: hidden;
  }
  .cap-band {
    position: absolute; left: 0; top: 0; width: 100%; height: 86px;
    background:
      linear-gradient(180deg, rgba(255,255,255,.9) 0 6px, transparent 6px 80px, rgba(0,0,0,.06) 80px),
      repeating-linear-gradient(90deg, var(--cap-white) 0 3px, var(--cap-ridge) 3px 4px, #ffffff 4px 6px);
  }
  .bottle-body {
    position: absolute; left: 0; top: 86px; width: 100%; height: 492px;
    background: linear-gradient(180deg, var(--orange-deep) 0 4px, var(--orange) 4px 80%, var(--orange-deep) 100%);
  }
  .bottle-body .ring {
    position: absolute; left: 0; width: 100%; height: 2px;
    background: linear-gradient(90deg, rgba(245,188,146,.2), rgba(245,188,146,.8), rgba(245,188,146,.2));
  }
  .ring-1 { top: 28px; }
  .ring-2 { top: 52px; }
  .label {
    position: absolute; left: 368px; top: 162px; width: 304px; height: 358px;
    background: var(--label); border-radius: 26px; color: var(--ink);
    font-family: "Roboto Mono", monospace;
  }
  .label > * { position: absolute; }
  .rx-glass { left: 42px; top: 22px; width: 44px; height: 70px; }
  .strength { left: 97px; top: 20px; font-size: 12.5px; font-weight: 500; letter-spacing: .2px; white-space: nowrap; }
  .product-name { left: 97px; top: 36px; font-family: "Oswald", sans-serif; font-weight: 700; font-size: 66px; line-height: 1; letter-spacing: 1px; }
  .bar { background: var(--yellow); left: 31px; }
  .bar-main { top: 100px; width: 242px; height: 12px; }
  .bar-mid { top: 146px; width: 242px; height: 4px; }
  .bar-low { top: 305px; width: 210px; height: 4px; }
  .meta { left: 31px; font-size: 11px; font-weight: 700; line-height: 14px; white-space: nowrap; }
  .meta-rx { top: 117px; }
  .for-title { left: 31px; top: 150px; font-family: "Oswald", sans-serif; font-size: 22px; line-height: 1.2; letter-spacing: 1px; }
  .directions {
    left: 31px; top: 180px; width: 242px; height: 64px; border: 1px solid var(--box-line);
    padding: 3px 5px; font-size: 10.4px; line-height: 14px; white-space: nowrap;
  }
  .warning { left: 31px; top: 249px; font-size: 10.4px; line-height: 14px; white-space: nowrap; }
  .warning strong { font-weight: 700; }
  .refill { top: 315px; }
  .stamp { left: 248px; top: 286px; width: 88px; height: 88px; }
</style>
</head>
<body>
  <main class="wrap-artwork">
    <div class="cap-band"></div>
    <div class="bottle-body">
      <span class="ring ring-1"></span>
      <span class="ring ring-2"></span>
    </div>
    <section class="label">
      <svg class="rx-glass" viewBox="0 0 44 70" role="img" aria-label="Orange wine glass icon with Rx lettering">
        <circle cx="22" cy="22" r="21" fill="#ee7325"/>
      </svg>
      <p class="strength">PRESCRIPTION STRENGTH</p>
      <h1 class="product-name">VINO</h1>
      <span class="bar bar-main"></span>
      <p class="meta meta-rx">RX #: GRAPE-ELIXIR<br>DR. GOOD CHEER</p>
      <span class="bar bar-mid"></span>
      <h2 class="for-title">FOR:</h2>
      <p class="directions">TAKE 2-6 OZ BY MOUTH TO RELIEVE<br>STRESS, END BAD DAYS, AND FORGET<br>THE HATERS. REPEAT AS NEEDED OR<br>UNTIL BOTTLE IS EMPTY.</p>
      <p class="warning"><strong>WARNING:</strong><br>SIDE EFFECTS COULD INCLUDE SILLINESS,<br>LOTS OF LAUGHTER AND FORGETTING OF<br>LIFE’S STRESSES.</p>
      <span class="bar bar-low"></span>
      <p class="meta refill">REFILLS: YES!<br>EXPIRES: WHEN EMPTY</p>
      <svg class="stamp" viewBox="0 0 88 88" aria-hidden="true">
        <circle cx="44" cy="44" r="41" fill="none" stroke="#a3262a" stroke-width="3" opacity=".85"/>
      </svg>
    </section>
  </main>
</body>
</html>
```